Business Card For Nightclub Industry

We're looking for a business card for our company GlintPulse. We're interested in finishing options including die-cut, foil, 2 opposing rounded corners (not 4 rounded corners) and spot UV.

The card should be elegant yet refined to reflect a high tech company.

The front of the cart should be bold with the glintpulse logo across. IF you choose to use a foil option, apply it to the glintpulse logo.

The back of the card will list our other company and product logos along with their related text and links.

Target Market(s)

video professionals
club owners
event promoters
nightclubs
DJs

Industry/Entity Type

Business

Contact Information for Business Card

Dario Fenwick
Founder & CEO

GlintPulse LLC <-- this line is optional as it is implied from the main logo
742 W. Calder Row
Austin, TX 78519
888.412.3096 x517

Font styles to use
Sans Serif

Requirements
Must have
• Front side logo:
• GlintPulse (logo attached)
• Premium Visuals For Live Events
• www.glintpulse-example.com
• --------
• Back side of card logos (equal sizing):
• GlintMarks (use glintpulse logo as placeholder; we are working on that logo now)
• Custom 3D Logo Animations
• www.glintmarks-example.com
• GlintBeams (use glintpulse logo as placeholder; we are working on that logo now)
• Professional Laser Systems
• www.glintbeams-example.com
• Quavix (logo)
• Visual Software & Media Servers
• www.quavix-example.net
• ReelCanvasHQ (logo)
• Premixed DVDs & BluRay
• www.discprisma-example.com
• Additional logos to add:
• ZephyrClips (logo)
• Cascade Fetchmaster (logo)
• Halberd Optics (logo)
• Clipnok (logo)
Nice to have
• Spot UV
• Foil
• Opposing Rounded Corners
• Matches the feel of our new website (attached pic)
• You are not required to implement the exact logo colors as they appear in the attachments. For instance, if you want to replace all the logos with chrome this might be a good option.

```html
<!DOCTYPE html>
<html lang="en">
<head>
<meta charset="utf-8">
<title>GlintPulse Business Cards</title>
<link href="https://fonts.googleapis.com/css2?family=Exo+2:wght@300;400;700&display=swap" rel="stylesheet">
<style>
  :root {
    --bg: #e9e4dc;
    --card-top: #222222;
    --card-bottom: #111111;
    --orange: #f26a1b;
    --white: #f2f2f2;
    --grey: #8a8a8a;
    --dim: #4a4a4a;
    --radius: 110px;
  }
  * { margin: 0; padding: 0; box-sizing: border-box; }
  html, body {
    width: 1200px;
    height: 900px;
    overflow: hidden;
    background: var(--bg);
    font-family: "Exo 2", sans-serif;
  }
  .canvas { position: relative; width: 1200px; height: 900px; }

  .card {
    position: absolute;
    width: 620px;
    height: 360px;
    border-radius: var(--radius) 0 var(--radius) 0;
    background: linear-gradient(160deg, var(--card-top), var(--card-bottom));
    box-shadow: 0 18px 40px rgba(0,0,0,0.25);
    color: var(--white);
  }
  .card--logos { left: 90px; top: 90px; }
  .card--contact { left: 490px; top: 450px; }

  /* wordmark: plain text plus one circle */
  .wordmark { display: flex; align-items: center; gap: 10px; }
  .wordmark__dot {
    width: 28px; height: 28px; border-radius: 50%;
    background: var(--orange);
  }
  .wordmark__name { font-weight: 700; color: var(--white); letter-spacing: 0.5px; }

  /* logos side */
  .sister-brands {
    position: absolute; top: 36px; right: 44px;
    display: flex; gap: 28px;
    font-size: 15px; font-weight: 400; color: var(--dim);
  }
  .hero {
    position: absolute; left: 0; right: 0; top: 118px;
    display: flex; flex-direction: column; align-items: center;
  }
  .hero .wordmark__dot { width: 44px; height: 44px; }
  .hero .wordmark__name { font-size: 40px; }
  .tagline {
    margin-top: 14px; font-size: 15px; font-weight: 300;
    color: var(--grey); letter-spacing: 1px;
  }
  .partner-row {
    position: absolute; left: 60px; right: 44px; bottom: 40px;
    display: flex; justify-content: space-between; align-items: center;
    font-size: 13px; font-weight: 700; color: var(--dim);
  }

  /* contact side */
  .contact-logo {
    position: absolute; left: 0; right: 0; top: 70px;
    display: flex; justify-content: center;
  }
  .contact-logo .wordmark__dot { width: 24px; height: 24px; }
  .contact-logo .wordmark__name { font-size: 24px; }
  .person { position: absolute; left: 150px; top: 160px; }
  .person__name { font-size: 26px; font-weight: 400; color: var(--white); }
  .person__title { font-size: 16px; font-weight: 300; color: var(--grey); margin-top: 4px; }
  .details {
    position: absolute; left: 150px; top: 240px;
    font-size: 15px; font-weight: 300; color: #bdbdbd; line-height: 1.45;
  }
</style>
</head>
<body>
<main class="canvas">

  <section class="card card--logos" aria-label="Card side with company and partner brands">
    <div class="sister-brands">
      <span class="sister-brands__item">GlintMarks</span>
      <span class="sister-brands__item">GlintBeams</span>
    </div>
    <div class="hero">
      <div class="wordmark">
        <span class="wordmark__dot"></span>
        <span class="wordmark__name">glintpulse</span>
      </div>
      <p class="tagline">Premium Visuals For Live Events</p>
    </div>
    <div class="partner-row">
      <span>Cascade Fetchmaster</span>
      <span>Quavix</span>
      <span>Halberd Optics</span>
      <span>ZephyrClips</span>
      <span>ReelCanvasHQ</span>
    </div>
  </section>

  <section class="card card--contact" aria-label="Card side with contact details">
    <div class="contact-logo">
      <div class="wordmark">
        <span class="wordmark__dot"></span>
        <span class="wordmark__name">glintpulse</span>
      </div>
    </div>
    <div class="person">
      <p class="person__name">Dario Fenwick</p>
      <p class="person__title">Founder &amp; CEO</p>
    </div>
    <address class="details" style="font-style: normal;">
      888.412.3096 x517<br>
      www.glintpulse-example.com<br>
      742 W. Calder Row Austin, TX 78519
    </address>
  </section>

</main>
</body>
</html>
```